Layla Karim Haddad Desert Fragrances

All our perfumes are non-alcoholic and water based. We want to have a design that would have some Arabic calligraphy, arabesque etc. We would be the label theme u design for all our scents. Of course, the scent flavor would changed. We will also use the pattern on the packaging of the scent as well. Something along the lines of this brand: http://veridocrest.example/en/.
Label size: Length 6"; Height 5"

Target Market(s)

middle east (Kuwait, UAE, Saudi Arabia);

Requirements
Must have
• 1. Flavor Name (editable)
• 2. Quantity 240 ml / 100 ml (editable)
• 3. Flavor Description (editable. each flavor has its own unique description)
• 4. Logo (place where we can display our logo. Logo file submitted.)
• 5. Company Name (editable. I should be able to edit this field too.)
Nice to have
• Flavor name in English and Arabic. You don't have to do any translation. Just make a space for us so that we can type-in the Arabic name. It wud be good to place the Arabic flavor name right below the English one.
Should not have
• images of animals, people

```html
<!DOCTYPE html>
<html lang="en">
<head>
<meta charset="utf-8">
<title>Flavor – Non-Alcoholic Fragrance Label</title>
<link rel="stylesheet" href="https://fonts.googleapis.com/css2?family=Marcellus&family=Amiri:wght@700&family=Arimo:wght@400&display=swap">
<style>
  :root {
    --backdrop: #f3efe6;
    --gold-light: #f1dca4;
    --gold-mid: #d9b66e;
    --gold-deep: #a9823f;
    --brown-top: #5a1a0a;
    --brown-deep: #2f0904;
    --brown-ink: #3a1106;
    --cream-text: #f4ead2;
    --gold-text: #e3c16f;
  }
  * { box-sizing: border-box; margin: 0; padding: 0; }
  html, body { width: 1200px; height: 1200px; overflow: hidden; }
  body { background: var(--backdrop); position: relative; font-family: "Arimo", sans-serif; }

  .label-panel {
    position: absolute;
    top: 110px;
    width: 380px;
    height: 980px;
    overflow: hidden;
    background: linear-gradient(90deg, var(--gold-deep) 0%, var(--gold-mid) 18%, var(--gold-light) 50%, var(--gold-mid) 82%, var(--gold-deep) 100%);
    box-shadow: 0 6px 24px rgba(60, 30, 10, 0.18);
  }
  .label-panel--front { left: 160px; }
  .label-panel--back { left: 660px; }

  .top-rule { position: absolute; left: 0; right: 0; top: 0; height: 16px; background: var(--brown-top); }
  .top-rule::after { content: ""; position: absolute; left: 0; right: 0; bottom: -6px; height: 2px; background: var(--brown-top); }
  .lace-band {
    position: absolute; left: 0; right: 0; top: 28px; height: 56px;
    background: linear-gradient(180deg, rgba(169,130,63,0.55), rgba(169,130,63,0.15));
  }
  .lower-field {
    position: absolute; left: 0; right: 0; top: 445px; bottom: 0;
    background: linear-gradient(180deg, var(--brown-top) 0%, var(--brown-deep) 100%);
  }
  .arabesque-band {
    position: absolute; left: 0; right: 0; top: 445px; height: 130px;
    background: linear-gradient(180deg, #b58a45 0%, #8a5f28 45%, rgba(90,26,10,0.2) 100%);
  }
  .arabesque-band::before {
    content: ""; position: absolute; left: 0; right: 0; top: 0; height: 3px; background: var(--gold-light);
  }

  .brand-mark {
    position: absolute; left: 0; right: 0;
    display: flex; align-items: center; justify-content: center; gap: 8px;
    font-family: "Marcellus", serif; color: var(--brown-ink);
  }
  .brand-mark__dot { border-radius: 50%; border: 2px solid var(--brown-ink); }
  .label-panel--front .brand-mark { top: 232px; font-size: 20px; }
  .label-panel--front .brand-mark__dot { width: 18px; height: 18px; }
  .label-panel--back .brand-mark { top: 160px; font-size: 15px; }
  .label-panel--back .brand-mark__dot { width: 13px; height: 13px; }

  .flavor-title { position: absolute; left: 0; right: 0; text-align: center; }
  .flavor-title__en {
    display: inline-block; font-family: "Marcellus", serif; letter-spacing: 3px;
    padding: 0 6px 6px; border-bottom: 2px solid currentColor;
  }
  .flavor-title__ar { display: block; font-family: "Amiri", serif; font-weight: 700; line-height: 1.1; margin-top: 2px; }

  .label-panel--front .flavor-title { top: 655px; color: var(--gold-text); }
  .label-panel--front .flavor-title__en { font-size: 52px; }
  .label-panel--front .flavor-title__ar { font-size: 46px; }

  .label-panel--back .flavor-title { top: 258px; color: var(--brown-ink); }
  .label-panel--back .flavor-title__en { font-size: 40px; }
  .label-panel--back .flavor-title__ar { font-size: 36px; }

  .volume {
    position: absolute; left: 0; right: 0; top: 902px; text-align: center;
    font-family: "Marcellus", serif; font-size: 27px; letter-spacing: 2px; color: var(--cream-text);
  }
  .fragrance-type {
    position: absolute; left: 0; right: 0; top: 410px; text-align: center;
    font-family: "Marcellus", serif; font-size: 18px; letter-spacing: 0.5px; color: var(--brown-ink);
  }
  .flavor-description {
    position: absolute; left: 18px; right: 18px; top: 612px; text-align: center;
    font-size: 16.5px; line-height: 1.3; color: var(--cream-text);
  }
  .origin {
    position: absolute; left: 0; right: 0; top: 870px; text-align: center;
    font-family: "Marcellus", serif; font-size: 17px; letter-spacing: 1px; color: var(--cream-text);
  }
</style>
</head>
<body>

<section class="label-panel label-panel--front" aria-label="Front label">
  <div class="top-rule"></div>
  <div class="lace-band" role="img" aria-label="Fine gold arabesque lace border"></div>
  <div class="brand-mark"><span class="brand-mark__dot"></span><span>Layla Karim Haddad</span></div>
  <div class="lower-field"></div>
  <div class="arabesque-band" role="img" aria-label="Ornate gold arabesque scrollwork band with central pendant motif"></div>
  <div class="flavor-title">
    <span class="flavor-title__en">FLAVOR</span>
    <span class="flavor-title__ar" lang="ar" dir="rtl">نكهة</span>
  </div>
  <div class="volume">240 ML</div>
</section>

<section class="label-panel label-panel--back" aria-label="Back label">
  <div class="top-rule"></div>
  <div class="lace-band" role="img" aria-label="Fine gold arabesque lace border"></div>
  <div class="brand-mark"><span class="brand-mark__dot"></span><span>Layla Karim Haddad</span></div>
  <div class="flavor-title">
    <span class="flavor-title__en">FLAVOR</span>
    <span class="flavor-title__ar" lang="ar" dir="rtl">نكهة</span>
  </div>
  <div class="fragrance-type">NON-ALCOHOLIC FRAGRANCE</div>
  <div class="lower-field"></div>
  <div class="arabesque-band" role="img" aria-label="Ornate gold arabesque scrollwork band with central pendant motif"></div>
  <p class="flavor-description">All our perfumes are non-alcoholic and water based. We want to have a design that would have some Arabic calligraphy, arabesque etc. We would be the label theme u design for all our scents. Of course, the scent flavor would changed. We will also use the pattern on the packaging of the scent as well.</p>
  <div class="origin">PRODUCT OF KUWAIT</div>
</section>

</body>
</html>
```